www.tarnebluvion.net

Hi,
UPDATE: Logo attached
TAG LINE NEW: OBITUARIES * CONDOLENCE NOTES
MULTIMEDIA MEMORIAL
Please refer to our existing site for more explanation of who we are?
We are a global data collecting portal site managing the Jewish funeral industry where users:
a) family and freinds in grief or "ancestry" searching persons
b) chevra kadisha's (funeral parlor)
c) current and historic cemetaries
d) Jewish Media Partners
arrive and choose a function (category):
in order to:
- upload a basic listing (FREE)
- upload/upgrade a multimedia listing (PAID)
- or search for a listing
of a deceased person (potentially millions of entries)
The functions (or categories) are accessed after the user:
Chooses their global location of search by
"Choose your Location" ie: Australia/NZ (which country?)
and allows the USER to choose a category function such as:
GROUP A (Local Info) GROUP B (Soul Search)
Chevra Kadisha Funerals (within 7 days)
Cemetaries Recently Deceased (up to 12mth)
Stonemasons Soul Search (after 1 year)
Jewish Media Partners
GROUP C (Jewish Death & Mourning Customs)
The way of Jewish burial
3000 y/old customs
When will Moshiach Come ?
Will I see my loved one again?
AIM:
To utilize existing logo and side menus (Member, Main & Resources) to create a user freindly and simpler friendly landing page, warmer and more softer for viewers.
To create logo buttons for the service catogories:
A, B & C and separate sub catagories
The MAIN AIM is to offer users opportunity to upload (LOG-IN required)
a) NEW basic FREE listing
b) NEW Multi-media PAID listing
SUMMARY:
1) User arrives at landing paid and sees global map, where he/she must choose the location in order to localize his data search
At this point, he/she can see what the site offers by the side MAIN, menu and icon function/catagories
(ie: Soul Search, New Basic Listing, Multimedia Listing)
2) After arriving at location (ie: Australia/NZ), the user then chooses the sub-function icon:
A- Local Funeral Service Info (Chevra Kadisha, Cemetary etc)
B- Soul Search (Funeral,Recently Deceased, Soul Search)
C- Jewish Death & Mourning Cutoms
Updates
Hi
Reason: Because of the holidays, we are happy to extend the deadline....
happy times
Target Market(s)
Family persons (Guest Member) & Industry (Members)
Industry/Entity Type
Industry
Requirements
Must have
- Style : Simple, Neat & Easy to Navigate
Icons: for each catagory/function
Colors; natural
-
Ability to bring inspiration, hope, light and healing to a difficult subject matter. (site look)
-
Education a profoundly deep 3000 y/old historically rich and mystic tradition to a wide audience
-
Allow children to access and upload data about grandparents etc
-
To promote on landing page the Invitation of local Chevra Kadisha's (funeral parlors), who have no web exposure, to get involved and LOG-IN and upload basic or multimedia listings.
(ie: please Register your local Chevra Kadisha here)
-
To promote on the landing page sample listings (Recently Deceased), to show look/feel of listings

```html
<!DOCTYPE html>
<html lang="en">
<head>
<meta charset="utf-8">
<title>Tarnebluvion.net – Global Chevra Kadisha network</title>
<link rel="stylesheet" href="https://fonts.googleapis.com/css2?family=Cormorant+Garamond:wght@400;500&family=Arimo:wght@400&display=swap">
<style>
  :root {
    --brown: #6e3a0c;
    --orange: #f07d0a;
    --orange-dark: #c8650a;
    --blue: #2d7fe0;
    --blue-dark: #1e66c6;
    --map-blue: #4aa6ee;
    --ink: #1a1a1a;
    --grey-text: #555;
    --band-light: #f6f6f6;
    --band-mid: #e2e2e2;
    --white: #ffffff;
    --serif: "Cormorant Garamond", Georgia, serif;
    --sans: "Arimo", Arial, sans-serif;
  }
  * { box-sizing: border-box; margin: 0; padding: 0; }
  html, body { width: 1000px; height: 1200px; overflow: hidden; background: var(--white); }
  body { position: relative; font-family: var(--sans); color: var(--ink); }
  .abs { position: absolute; }

  /* Region strip */
  .region-strip { left: 0; top: 0; width: 1000px; height: 35px; }
  .region-links { right: 0; top: 0; height: 35px; display: flex; align-items: center; font-size: 13px; }
  .region-links span { padding: 0 10px; color: var(--orange); border-left: 1px solid rgba(255,255,255,.12); line-height: 22px; }
  .region-links span:first-child { border-left: 0; color: var(--white); }

  /* Brand */
  .brand { left: 52px; top: 52px; display: flex; align-items: center; gap: 10px; font-family: var(--serif); font-size: 27px; color: #222; }
  .brand-dot { width: 14px; height: 14px; border-radius: 50%; background: var(--orange); }

  .search { left: 737px; top: 82px; width: 188px; height: 24px; border-radius: 8px; background: #eeeeee; font-size: 11px; color: #aaa; padding: 5px 10px; }
  .search svg { position: absolute; right: 8px; top: 3px; }

  /* Navigation bands */
  .nav-band { left: 0; width: 1000px; height: 36px; background: linear-gradient(var(--band-light), var(--band-mid)); }
  .nav-band.top { top: 123px; }
  .nav-band.bottom { top: 1095px; height: 46px; background: linear-gradient(#ececec, #fafafa); border-bottom: 1px solid #ddd; }
  .nav { position: absolute; top: 0; height: 100%; display: flex; align-items: center; font-family: var(--serif); font-size: 19px; color: #444; }
  .nav span { margin-right: 35px; }
  .nav-home { background: #d9d9d9; padding: 5px 17px; border-radius: 0 0 4px 4px; }

  /* Slider */
  .slider-shadow { left: 0; top: 165px; width: 1000px; height: 370px; background: radial-gradient(ellipse at 50% 100%, rgba(0,0,0,.18), transparent 60%); }
  .slider-frame { left: 30px; top: 169px; width: 940px; height: 345px; background: var(--white); box-shadow: 0 4px 10px rgba(0,0,0,.25); }
  .slider-photo { left: 34px; top: 169px; width: 932px; height: 304px; border-radius: 8px 8px 0 0;
    background: radial-gradient(ellipse at 48% 45%, #d9862c 0%, #b8661c 30%, #e7c8a2 62%, #f2e3cf 100%); }
  .slider-caption { left: 30px; top: 478px; width: 940px; text-align: center; font-family: var(--serif); font-size: 23px; color: #222; }
  .slider-arrow { top: 323px; width: 39px; height: 39px; border-radius: 6px; background: var(--orange-dark); }
  .slider-arrow.prev { left: 26px; }
  .slider-arrow.next { left: 934px; }
  .slider-arrow svg { display: block; margin: 11px auto 0; }

  /* Intro */
  .intro-title { left: 30px; top: 556px; font-family: var(--serif); font-size: 25px; color: #222; }
  .intro-text { left: 30px; top: 591px; width: 935px; font-size: 12.5px; line-height: 24px; color: var(--ink); }

  /* Category tabs */
  .tabs { left: 31px; top: 700px; width: 649px; height: 28px; border-radius: 7px; background: linear-gradient(#f3f3f3, #d6d6d6); font-size: 13px; }
  .tabs span { position: absolute; top: 6px; }
  .tab-active { left: 153px; top: 695px; width: 99px; height: 33px; background: #d0d0d0; border-top: 3px solid #111; border-radius: 8px 8px 0 0; }
  .dropdown { left: 157px; top: 728px; width: 266px; height: 103px; background: #d3d3d3; font-size: 12px; }
  .dropdown div { height: 24px; padding: 4px 10px; }
  .dropdown div:first-child { background: #ececec; }

  .region-select { left: 529px; top: 736px; width: 147px; height: 28px; border-radius: 8px; border: 1px solid #c8c8c8;
    background: linear-gradient(#fafafa, #dedede); font-size: 13px; padding: 6px 14px; box-shadow: 0 2px 3px rgba(0,0,0,.2); }
  .region-select i { position: absolute; right: 30px; top: 2px; bottom: 2px; border-left: 1px solid #bbb; }
  .region-select svg { position: absolute; right: 11px; top: 10px; }

  .world-map { left: 40px; top: 798px; width: 525px; height: 272px; border-radius: 40px;
    background: linear-gradient(160deg, #7cc2f5, var(--map-blue) 55%, #2b86d6); opacity: .9; }

  /* Login panels */
  .login { left: 693px; width: 274px; height: 132px; border-radius: 5px; }
  .login.free { top: 703px; background: linear-gradient(var(--blue), var(--blue-dark)); border: 1px solid #1b5bb0; }
  .login.paid { top: 883px; background: linear-gradient(#fbaa3c, var(--orange)); border: 1px solid #d7780c; }
  .login h2 { position: absolute; left: 22px; top: 5px; font-weight: 400; font-size: 23px; color: var(--white); }
  .field { position: absolute; left: 15px; width: 242px; height: 24px; border-radius: 8px; background: var(--white); font-size: 12px; color: #666; padding: 5px 15px; }
  .field.user { top: 43px; }
  .field.pass { top: 76px; }
  .sign-in { position: absolute; left: 87px; top: 113px; width: 102px; height: 25px; border-radius: 7px;
    background: linear-gradient(#ffffff, #d8d8d8); text-align: center; font-size: 16px; padding-top: 2px; color: var(--ink); }
  .login-note { right: 37px; font-size: 12px; color: var(--ink); }

  .copyright { left: 20px; top: 1152px; font-size: 12px; color: #999; }
  .social { left: 807px; top: 1155px; display: flex; gap: 10px; }
  .social span { width: 21px; height: 21px; border-radius: 3px; }
</style>
</head>
<body>

  <svg class="abs region-strip" width="1000" height="35" aria-hidden="true">
    <polygon points="255,0 1000,0 1000,35 290,35" fill="#6e3a0c"/>
  </svg>
  <nav class="abs region-links">
    <span>Australia/NZ</span><span>Canada</span><span>United States</span><span>Israel</span><span>Europe</span><span>UK</span><span>Asia</span><span>Central and South America</span><span>Africa</span>
  </nav>

  <div class="abs brand"><span class="brand-dot"></span>Tarnebluvion.net</div>

  <div class="abs search">Search
    <svg width="20" height="18" viewBox="0 0 20 18"><circle cx="8" cy="8" r="5.5" fill="none" stroke="#777" stroke-width="1.8"/><line x1="12" y1="12" x2="17" y2="16" stroke="#777" stroke-width="2.4" stroke-linecap="round"/></svg>
  </div>

  <div class="abs nav-band top">
    <div class="nav" style="left:128px">
      <span class="nav-home">Home</span><span>Our mission</span><span>About Us</span><span style="margin-right:42px">Personal Media</span><span>Contact Us</span><span>On-line Forum</span>
    </div>
  </div>

  <div class="abs slider-shadow"></div>
  <div class="abs slider-frame"></div>
  <div class="abs slider-photo" role="img" aria-label="Golden Star of David resting on a page of Hebrew text"></div>
  <p class="abs slider-caption">Welcome to the global Chevra Kadisha network</p>
  <div class="abs slider-arrow prev"><svg width="14" height="17"><polygon points="12,0 12,17 0,8.5" fill="#fff"/></svg></div>
  <div class="abs slider-arrow next"><svg width="14" height="17"><polygon points="2,0 2,17 14,8.5" fill="#fff"/></svg></div>

  <h1 class="abs intro-title" style="font-weight:400">Please choose your region</h1>
  <p class="abs intro-text">Tarnebluvion.net is the global Jewish community's sacred burial society's website and resource portal, for data collation of personal media (obituaries, condolence comments, photos &amp; video), relating to Jewish persons who have passed on, for use by service providers and relatives today and in successive generations.<br>Here you can find details information about your local Chevra Kadisha and support services, such as Cemeteries, Stonemasons and Jewish Newspapers. Other categories include:</p>

  <div class="abs world-map" role="img" aria-label="World map for choosing a region"></div>

  <div class="abs tabs">
    <span style="left:29px">Local Info</span>
    <span style="left:257px">Jewish Death &amp; Mourning Customs</span>
  </div>
  <div class="abs tab-active"></div>
  <span class="abs" style="left:167px;top:706px;font-size:13px">Soul Search</span>
  <div class="abs dropdown">
    <div>Chevra Kadisha Funerals (within 7 days)</div>
    <div>Cemetaries Recently Deceased (up to 12mth)</div>
    <div>Stonemasons Soul Search (after 1 year)</div>
    <div>Jewish Media Partners</div>
  </div>

  <div class="abs region-select">Australia/NZ<i></i>
    <svg width="10" height="8"><polygon points="0,0 10,0 5,8" fill="#222"/></svg>
  </div>

  <section class="abs login free">
    <h2>Free listing</h2>
    <div class="field user">Username</div>
    <div class="field pass">Password</div>
    <div class="sign-in">Sign in</div>
  </section>
  <p class="abs login-note" style="top:846px">normal upload</p>

  <section class="abs login paid">
    <h2>Paid listings</h2>
    <div class="field user">Username</div>
    <div class="field pass">Password</div>
    <div class="sign-in">Sign in</div>
  </section>
  <p class="abs login-note" style="top:1028px;right:35px">multimedia upload like video / audio etc...</p>

  <div class="abs nav-band bottom">
    <div class="nav" style="left:163px">
      <span>Home</span><span>Our mission</span><span>About Us</span><span style="margin-right:42px">Personal Media</span><span>Contact Us</span><span>On-line Forum</span>
    </div>
  </div>

  <p class="abs copyright">Copyright © 2011. www.tarnebluvion.com</p>
  <div class="abs social" aria-label="Social links">
    <span style="background:#3b5a9a"></span>
    <span style="background:#4fb6e6"></span>
    <span style="background:#f08a1e"></span>
    <span style="background:#1f6fa8"></span>
    <span style="background:#2f6fb8"></span>
  </div>

</body>
</html>
```